Birch Harbor - Countertop fabricator
Need stationary, business card and T-shirt design
Birch Harbor - Countertop fabricator -
Creative Brief
Simple
Kevin Rasble
14 Larkwood Lane Syracuse, NY13099
info@birchharborny.example
www.birchharborny.example
Back of card to list materials; Granite Quatz Marble Soapstone Solid Surface

```html
<!DOCTYPE html>
<html lang="en">
<head>
<meta charset="utf-8">
<title>Birch Harbor Stationery</title>
<link href="https://fonts.googleapis.com/css2?family=Lato:wght@400;700&display=swap" rel="stylesheet">
<style>
  :root {
    --bg: #e6e6e6;
    --paper: #ffffff;
    --brown: #7a5530;
    --brown-dark: #5e3f20;
    --gold: #c9a86a;
    --beige: #ece4d6;
    --ink: #6b5a48;
    --rule: #b9a58a;
    --card-text: #f3e9d8;
  }
  * { box-sizing: border-box; margin: 0; padding: 0; }
  html, body { width: 1200px; height: 816px; overflow: hidden; }
  body {
    background: var(--bg);
    font-family: "Lato", Arial, sans-serif;
    color: var(--ink);
    position: relative;
  }
  address { font-style: normal; }
  .piece {
    position: absolute;
    background: var(--paper);
    box-shadow: 0 3px 10px rgba(0,0,0,0.22);
    overflow: hidden;
  }
  .brand {
    display: flex; align-items: center; gap: 8px;
    color: var(--brown); font-weight: 700; white-space: nowrap;
  }
  .brand-square { background: var(--brown); flex: none; }
  .bar {
    position: absolute; left: 0; right: 0;
    background: linear-gradient(90deg, var(--brown-dark), var(--gold) 60%, rgba(201,168,106,0));
  }
  .contact {
    position: absolute; border-left: 1px solid var(--rule);
    line-height: 1.45; white-space: nowrap;
  }
  .block { position: absolute; background: var(--beige); }

  /* Letterhead */
  .letterhead { left: 24px; top: 72px; width: 523px; height: 677px; }
  .letterhead .bar-top { top: 8px; left: 70px; height: 4px; }
  .letterhead .bar-bottom { bottom: 10px; height: 4px; }
  .letterhead .brand { position: absolute; left: 18px; top: 22px; font-size: 22px; }
  .letterhead .brand-square { width: 22px; height: 22px; }
  .letterhead .contact { left: 342px; top: 12px; padding-left: 8px; font-size: 9px; }
  .letterhead .block { right: 0; bottom: 28px; width: 170px; height: 120px; }

  /* Business card front */
  .card-front { left: 648px; top: 65px; width: 223px; height: 103px; }
  .card-front .bar-top { top: 3px; left: 30px; height: 2px; }
  .card-front .bar-bottom { bottom: 4px; height: 2px; }
  .card-front .brand { position: absolute; left: 10px; top: 12px; font-size: 11px; gap: 5px; }
  .card-front .brand-square { width: 11px; height: 11px; }
  .card-front .contact { left: 112px; top: 7px; padding-left: 5px; font-size: 5.5px; }
  .card-front .name { font-size: 7px; font-weight: 700; color: var(--brown); margin-bottom: 1px; }
  .card-front .title { margin-bottom: 5px; }

  /* Business card back */
  .card-back {
    left: 890px; top: 65px; width: 226px; height: 103px;
    background: linear-gradient(180deg, #8a6238, var(--brown-dark));
  }
  .materials {
    position: absolute; left: 14px; top: 10px; list-style: none;
    color: var(--card-text); font-size: 7px; line-height: 1.75;
  }
  .materials li::before { content: "\25A0"; font-size: 4px; margin-right: 6px; vertical-align: 2px; }
  .card-back .block { background: var(--paper); right: 0; bottom: 10px; width: 70px; height: 56px; }

  /* Envelope front */
  .envelope { left: 581px; top: 216px; width: 547px; height: 252px; }
  .envelope .bar-top { top: 7px; left: 64px; height: 3px; }
  .envelope .bar-bottom { bottom: 8px; height: 3px; }
  .envelope .brand { position: absolute; left: 16px; top: 24px; font-size: 20px; }
  .envelope .brand-square { width: 20px; height: 20px; }
  .envelope .contact { left: 170px; top: 18px; padding-left: 7px; font-size: 8.5px; }
  .envelope .block { right: 0; bottom: 22px; width: 110px; height: 80px; }

  /* Envelope back */
  .envelope-back { left: 581px; top: 504px; width: 547px; height: 245px; }
  .envelope-back svg { position: absolute; left: 0; top: 0; }
</style>
</head>
<body>

<section class="piece letterhead">
  <div class="bar bar-top"></div>
  <div class="brand"><span class="brand-square"></span>BirchHarbor</div>
  <address class="contact">
    14 Larkwood Lane<br>Cedarford, EX 40912<br>Phone: 555-010-0142<br>Fax: 555-010-0187<br>www.birchharborny.example
  </address>
  <div class="block"></div>
  <div class="bar bar-bottom"></div>
</section>

<section class="piece card-front">
  <div class="bar bar-top"></div>
  <div class="brand"><span class="brand-square"></span>BirchHarbor</div>
  <address class="contact">
    <div class="name">Kevin Rasble</div>
    <div class="title">Owner</div>
    14 Larkwood Lane<br>Cedarford, EX 40912<br>Phone: 555-010-0142<br>Cell: 555-010-0163<br>Fax: 555-010-0187<br>info@birchharborny.example<br>www.birchharborny.example
  </address>
  <div class="bar bar-bottom"></div>
</section>

<section class="piece card-back">
  <ul class="materials">
    <li>Granite</li><li>Quartz</li><li>Marble</li><li>Soapstone</li><li>Solid Surface</li>
  </ul>
  <div class="block"></div>
</section>

<section class="piece envelope">
  <div class="bar bar-top"></div>
  <div class="brand"><span class="brand-square"></span>BirchHarbor</div>
  <address class="contact">
    14 Larkwood Lane<br>Cedarford, EX 40912
  </address>
  <div class="block"></div>
  <div class="bar bar-bottom"></div>
</section>

<section class="piece envelope-back">
  <svg width="547" height="245" viewBox="0 0 547 245" aria-hidden="true">
    <defs>
      <linearGradient id="flapFill" x1="0" y1="0" x2="0" y2="1">
        <stop offset="0" stop-color="#8a6238"/>
        <stop offset="1" stop-color="#5e3f20"/>
      </linearGradient>
    </defs>
    <path d="M0 0 H547 V6 L470 78 Q460 86 445 86 H102 Q87 86 77 78 L0 6 Z" fill="url(#flapFill)" stroke="#c9a86a" stroke-width="2"/>
  </svg>
</section>

</body>
</html>
```